KVO-Business Card Design

I need a modern, professional business card design that includes my logo as the main feature, maybe the entire background with the contact info overlaying or even contact info on the back and the logo full frontal

Neat and organized placement of contact information

Would like to see options in black and white

Target Market(s)

real estate Developers, Construction managers, business and home owners

Industry/Entity Type

Construction

Contact Information for Business Card

KVO Construction
Danny Ferrante
General Contractor

Office: 1-888-902-7315 Ext #1
Cell: 215-730-4162
Fax: 1-888-902-7315

Font styles to use
Serif

Requirements
Must have
• title
• office #
• cell #
• Email
• website
Nice to have
• fax

```html
<!DOCTYPE html>
<html lang="en">
<head>
<meta charset="utf-8">
<title>KVO Construction – Business Card</title>
<link rel="stylesheet" href="https://fonts.googleapis.com/css2?family=Roboto+Slab:wght@400;700;900&display=swap">
<style>
  :root {
    --ink: #1f1f1f;
    --paper: #ffffff;
    --lime: #6cc72a;
    --grey-text: #9a9a9a;
    --backdrop: #e6e6e6;
  }
  html, body {
    margin: 0;
    width: 1200px;
    height: 1200px;
    overflow: hidden;
    background: var(--backdrop);
  }
  .canvas {
    position: relative;
    width: 1200px;
    height: 1200px;
  }
  .card {
    position: absolute;
    left: 150px;
    width: 900px;
    height: 514px;
    background: var(--paper);
    overflow: hidden;
    box-shadow: 0 10px 30px rgba(0,0,0,0.18);
  }
  .card--front { top: 50px; }
  .card--back { top: 630px; }
  .card__shapes {
    position: absolute;
    inset: 0;
    width: 100%;
    height: 100%;
  }
  .wordmark {
    position: absolute;
    top: 130px;
    left: 0;
    right: 0;
    text-align: center;
    font-family: "Roboto Slab", serif;
    font-weight: 700;
    font-size: 64px;
    letter-spacing: 1px;
    color: var(--lime);
  }
  .website {
    position: absolute;
    left: 0;
    right: 0;
    text-align: center;
    font-family: "Roboto Slab", serif;
    font-weight: 400;
    font-size: 22px;
    letter-spacing: 7px;
    color: var(--grey-text);
  }
  .card--front .website { bottom: 42px; }
  .card--back .website { bottom: 26px; }
  .contact {
    position: absolute;
    left: 48px;
    top: 150px;
    margin: 0;
    padding: 0;
    list-style: none;
    font-family: "Roboto Slab", serif;
    font-size: 20px;
    line-height: 38px;
    color: var(--ink);
  }
  .identity {
    position: absolute;
    right: 56px;
    top: 220px;
    text-align: right;
    font-family: "Roboto Slab", serif;
    color: var(--ink);
  }
  .identity__name {
    margin: 0 0 10px;
    font-family: "Roboto Slab", serif;
    font-weight: 900;
    font-size: 42px;
    letter-spacing: 0;
  }
  .identity__line {
    margin: 0;
    font-size: 20px;
    line-height: 30px;
    letter-spacing: 1px;
  }
</style>
</head>
<body>
<main class="canvas">

  <section class="card card--front" aria-label="Card front">
    <svg class="card__shapes" viewBox="0 0 900 514" preserveAspectRatio="none" aria-hidden="true">
      <path d="M0 300 C250 330 600 300 900 372 V514 H0 Z" fill="var(--lime)"/>
      <path d="M0 316 C250 346 600 318 900 390 V514 H0 Z" fill="var(--ink)"/>
    </svg>
    <div class="wordmark">KVO Construction</div>
    <div class="website">www.kvoconstruction.net</div>
  </section>

  <section class="card card--back" aria-label="Card back">
    <svg class="card__shapes" viewBox="0 0 900 514" preserveAspectRatio="none" aria-hidden="true">
      <path d="M0 0 H900 V150 C700 210 420 60 0 118 Z" fill="var(--lime)"/>
      <path d="M0 0 H900 V134 C700 194 420 44 0 102 Z" fill="var(--ink)"/>
      <path d="M0 410 C300 372 600 452 900 392 V514 H0 Z" fill="var(--lime)"/>
      <path d="M0 426 C300 388 600 468 900 408 V514 H0 Z" fill="var(--ink)"/>
    </svg>
    <ul class="contact">
      <li>danny@kvoconstruction.net</li>
      <li>215-730-4162: Cell</li>
      <li>1-888-902-7315 Ext #1: OFFICE</li>
      <li>1-888-902-7315: Fax</li>
    </ul>
    <div class="identity">
      <h1 class="identity__name">Danny Ferrante</h1>
      <p class="identity__line">KVO Construction</p>
      <p class="identity__line">General Contractor</p>
    </div>
    <div class="website">www.kvoconstruction.net</div>
  </section>

</main>
</body>
</html>
```